Business Card (I don't have a logo)

I'm bootstrapping a new venture and need a business card and "look" for it. I'd like to print one side only, but could do a bleed to the edges, but don't need to. See my website: www.paulridgecapital.com to get a sense of the photos that relate to the look/feel of my company.

Target Market(s)

high tech start-up company CEO's in Silicon Valley

Industry/Entity Type

Business

Requirements
Must have
• a look that can cut/paste onto my website that integrates easily with the front page photo. see www.paulridgecapital.com

```html
<!DOCTYPE html>
<html lang="en">
<head>
<meta charset="utf-8">
<title>Paul Ridge Capital — Business Card</title>
<link rel="stylesheet" href="https://fonts.googleapis.com/css2?family=Roboto:wght@300;400&display=swap">
<style>
  :root {
    --page-bg: #ffffff;
    --card-white: #ffffff;
    --ink: #1f4a60;
    --band-dark: #0c4352;
    --band-mid: #1a8ba6;
    --band-text: #ffffff;
    --sea-dark: #3e454c;
    --sea-mid: #6b7379;
    --ice-light: #e3edf1;
    --ice-blue: #9fbecb;
    --ice-deep: #6f95a6;
  }
  html, body {
    margin: 0;
    padding: 0;
    width: 1200px;
    height: 721px;
    overflow: hidden;
    background: var(--page-bg);
  }
  .card {
    position: relative;
    width: 1200px;
    height: 721px;
    overflow: hidden;
    border-radius: 0 66px 0 66px;
    background: var(--card-white);
    font-family: "Roboto", Arial, sans-serif;
  }
  .photo-band {
    position: absolute;
    left: 0; top: 0;
    width: 100%;
    height: 167px;
    background:
      linear-gradient(180deg, rgba(255,255,255,0.55) 0%, rgba(255,255,255,0) 45%),
      linear-gradient(90deg, var(--sea-dark) 0%, var(--sea-mid) 28%, var(--sea-mid) 46%, var(--ice-light) 52%, var(--ice-blue) 70%, var(--ice-deep) 100%);
  }
  .accent-rule {
    position: absolute;
    left: 123px;
    top: 202px;
    width: 3px;
    height: 292px;
    background: var(--ink);
  }
  .company-name {
    position: absolute;
    left: 147px;
    top: 402px;
    margin: 0;
    font-size: 102px;
    line-height: 1;
    font-weight: 400;
    letter-spacing: -2px;
    color: var(--ink);
    white-space: nowrap;
  }
  .company-name .light { font-weight: 300; }
  .contact-band {
    position: absolute;
    left: 0; bottom: 0;
    width: 100%;
    height: 179px;
    background: linear-gradient(90deg, var(--band-dark) 0%, var(--band-mid) 55%, var(--band-dark) 100%);
  }
  .website {
    position: absolute;
    left: 149px;
    top: 566px;
    margin: 0;
    font-size: 30px;
    font-weight: 400;
    letter-spacing: 24px;
    color: var(--band-text);
    white-space: nowrap;
  }
</style>
</head>
<body>
  <main class="card">
    <div class="photo-band" role="img" aria-label="Photograph of expedition boats with passengers in red jackets beside a large blue iceberg"></div>
    <div class="accent-rule"></div>
    <h1 class="company-name">Paul Ridge <span class="light">Capital</span></h1>
    <div class="contact-band"></div>
    <p class="website">paulridgecapital.com</p>
  </main>
</body>
</html>
```